beauty salon

providing waxing services from a home base this must include which I will provide a price list and an address

Industry/Entity Type

Beauty Salon

Font styles to use
Script

Colors

Designer to choose colors to be used in the design.

```html
<!DOCTYPE html>
<html lang="en">
<head>
<meta charset="utf-8">
<title>Willow Rose Salon – Waxing Price List</title>
<link rel="stylesheet" href="https://fonts.googleapis.com/css2?family=Great+Vibes&family=Lato:wght@400;700&family=Montserrat:wght@900&display=swap">
<style>
  :root {
    --purple: #7b2f8e;
    --mauve: #9a4f9a;
    --ink: #222222;
    --panel-top: #d6eff2;
    --panel-bottom: #f4fbfc;
    --rule: #8ccfd6;
    --skin-light: #f6e6dc;
    --skin-mid: #e9c9b6;
    --white: #ffffff;
  }
  * { box-sizing: border-box; margin: 0; padding: 0; }
  html, body { width: 1200px; height: 850px; overflow: hidden; background: var(--white); }
  .flyer {
    position: relative;
    width: 1200px;
    height: 850px;
    overflow: hidden;
    background: var(--white);
    font-family: "Lato", "Helvetica Neue", Arial, sans-serif;
    color: var(--ink);
  }

  /* Photo area */
  .model-photo {
    position: absolute;
    left: 450px; top: 0;
    width: 440px; height: 850px;
    background: radial-gradient(ellipse at 50% 45%, var(--skin-mid) 0%, var(--skin-light) 45%, var(--white) 78%);
  }

  /* Price panel background */
  .panel-shape { position: absolute; left: 0; top: 0; width: 1200px; height: 850px; }

  /* Left column */
  .intro {
    position: absolute;
    left: 40px; top: 0;
    width: 460px;
    text-align: center;
  }
  .brand {
    position: absolute;
    top: 112px; left: 0; width: 100%;
    display: flex; align-items: center; justify-content: center; gap: 12px;
    font-size: 24px; font-weight: 700; color: var(--mauve);
    letter-spacing: 0.3px;
  }
  .brand-dot { width: 14px; height: 14px; border-radius: 50%; background: var(--mauve); }
  .therapist {
    position: absolute; top: 168px; left: 0; width: 100%;
    font-family: "Great Vibes", cursive; font-size: 40px; color: var(--ink);
  }
  .diploma {
    position: absolute; top: 221px; left: 0; width: 100%;
    font-size: 22px;
  }
  .contact {
    position: absolute; left: 0; width: 100%;
    font-size: 19px;
  }
  .contact-address { top: 260px; }
  .contact-mobile { top: 287px; }
  .contact .label { color: var(--purple); }

  .now-open {
    position: absolute; top: 360px; left: 0; width: 100%;
    font-family: "Great Vibes", cursive; font-size: 54px; color: var(--purple);
  }
  .hours {
    position: absolute; top: 424px; left: 30px;
    display: grid;
    grid-template-columns: 200px 22px auto;
    row-gap: 6px;
    font-size: 19px;
  }
  .hours .day { text-align: right; }
  .hours .dot { text-align: center; color: var(--purple); }

  .offer { position: absolute; left: 126px; top: 548px; width: 300px; height: 240px; }
  .offer-percent {
    position: absolute; left: 0; top: 0;
    font-family: "Montserrat", "Arial Black", sans-serif; font-weight: 900;
    font-size: 112px; line-height: 1; color: var(--purple); letter-spacing: -3px;
  }
  .offer-off {
    position: absolute; left: 238px; top: 14px;
    font-family: "Montserrat", "Arial Black", sans-serif; font-weight: 900;
    font-size: 44px; line-height: 1; color: var(--purple);
    transform-origin: left top;
    transform: rotate(90deg) translate(0, -52px);
    letter-spacing: 2px;
  }
  .offer-text {
    position: absolute; left: -4px; top: 104px; width: 320px;
    font-family: "Great Vibes", cursive; font-size: 58px; line-height: 0.98;
    color: var(--purple); text-align: center;
  }

  /* Price list */
  .price-list { position: absolute; left: 903px; top: 30px; width: 297px; }
  .price-group { margin-bottom: 28px; }
  .price-heading {
    font-size: 18px; font-weight: 700; color: var(--purple);
    letter-spacing: 0.8px; text-transform: uppercase;
    padding-bottom: 6px;
    border-bottom: 1px solid var(--rule);
    margin-left: -18px; padding-left: 18px;
    margin-bottom: 6px;
  }
  .price-row {
    display: grid; grid-template-columns: 171px auto;
    font-size: 19.5px; line-height: 27.6px;
  }
  .price-group.eye { margin-top: 0; }
</style>
</head>
<body>
<main class="flyer">

  <div class="model-photo" role="img" aria-label="Photograph of a smiling woman with long brown hair and a flower behind her ear, seated in white underwear hugging her smooth bare legs"></div>

  <svg class="panel-shape" viewBox="0 0 1200 850" aria-hidden="true">
    <defs>
      <linearGradient id="panelFill" x1="0" y1="0" x2="1" y2="0">
        <stop offset="0" stop-color="var(--panel-top)"/>
        <stop offset="0.25" stop-color="var(--panel-bottom)"/>
        <stop offset="1" stop-color="var(--white)"/>
      </linearGradient>
    </defs>
    <path d="M872 0 C 795 240 778 600 828 850 L 1200 850 L 1200 0 Z" fill="url(#panelFill)"/>
    <path d="M872 0 C 795 240 778 600 828 850" fill="none" stroke="var(--rule)" stroke-width="1.5"/>
  </svg>

  <section class="intro">
    <div class="brand"><span class="brand-dot"></span>Willow Rose Salon</div>
    <div class="therapist">Beauty Therapist : Marisa</div>
    <div class="diploma">Diploma of Beauty Therapy at Harlow College</div>
    <div class="contact contact-address"><span class="label">Address</span> 12 Finch Lane, Hillcrest</div>
    <div class="contact contact-mobile"><span class="label">Mobile</span> 0400 555 019</div>

    <div class="now-open">Now Open!</div>
    <div class="hours">
      <span class="day">Wednesdays</span><span class="dot">•</span><span class="time">10am to 4pm</span>
      <span class="day">Fridays</span><span class="dot">•</span><span class="time">10am to 7pm</span>
      <span class="day">Saturday</span><span class="dot">•</span><span class="time">10am to 4pm</span>
    </div>
  </section>

  <section class="offer">
    <div class="offer-percent">10%</div>
    <div class="offer-off">OFF</div>
    <div class="offer-text">Your First<br>Treatment</div>
  </section>

  <section class="price-list">
    <div class="price-group">
      <h2 class="price-heading">Lady’s Waxing</h2>
      <div class="price-row"><span>Eyebrow</span><span>$8</span></div>
      <div class="price-row"><span>Upper lip</span><span>$8</span></div>
      <div class="price-row"><span>Chin</span><span>$8</span></div>
      <div class="price-row"><span>Face wax</span><span>$25</span></div>
      <div class="price-row"><span>Bikini line</span><span>$15</span></div>
      <div class="price-row"><span>G string</span><span>$20</span></div>
      <div class="price-row"><span>½ Brazilian</span><span>$30</span></div>
      <div class="price-row"><span>Full Brazilian</span><span>$40</span></div>
      <div class="price-row"><span>Half arm</span><span>$20</span></div>
      <div class="price-row"><span>Upper half arm</span><span>$20</span></div>
      <div class="price-row"><span>Full arm</span><span>$25</span></div>
      <div class="price-row"><span>Half leg</span><span>$15</span></div>
      <div class="price-row"><span>Upper leg</span><span>$20</span></div>
      <div class="price-row"><span>¾ Leg</span><span>$25</span></div>
      <div class="price-row"><span>Full leg</span><span>$35</span></div>
    </div>
    <div class="price-group">
      <h2 class="price-heading">Men’s Waxing</h2>
      <div class="price-row"><span>Eyebrow</span><span>$10</span></div>
      <div class="price-row"><span>Half arm</span><span>$20</span></div>
      <div class="price-row"><span>Upper half arm</span><span>$25</span></div>
      <div class="price-row"><span>Full arm</span><span>$30</span></div>
      <div class="price-row"><span>Half leg</span><span>$25</span></div>
    </div>
    <div class="price-group eye">
      <h2 class="price-heading">Eye Enhancement</h2>
      <div class="price-row"><span>Eyebrow tint</span><span>$12</span></div>
      <div class="price-row"><span>Eyelash tint</span><span>$15</span></div>
    </div>
  </section>

</main>
</body>
</html>
```